Wedding Vow Design for Modern Print - SUBWAY PRINT STYLE or Similar, MODERN

I recently got married and I want to take the main words from my wedding vows and create a design using them that I can have printed and present to my new wife. I told her that I had privileges with Marring her and I made her promises. I would like to highlight both. We have a modern home and I want something that we can have professionally framed and hung on the wall. Love modern and clean design but something interesting.

Target Market(s)

Myself. 35, modern and loves clean design.

Industry/Entity Type

Wedding

Font styles to use
Serif

Colors
f6f3f8
ffffff
fbd4d5
000000
9d9d9d
dddddd

Requirements
Must have
• Cool, clean and modern design. Neutral Colors, Clean lines, Black and White, no reds, pinks, etc.
• We will hang this in our California modern home.
Nice to have
• Our wedding colors were , Gray,Black, Light Pink. I love the Subway signs and also love Black and White Word art.
Should not have
• Flowers, squiggly lines, traditional design. Something that would look great in a stainless metal frame or mirrored frame on white walls.

```html
<!DOCTYPE html>
<html lang="en">
<head>
<meta charset="UTF-8">
<title>Privileges and Promises</title>
<link href="https://fonts.googleapis.com/css2?family=Cormorant+Garamond:wght@300;500&display=swap" rel="stylesheet">
<style>
  :root {
    --heading: #e2d4d4;
    --heading-shadow: #000000;
    --item: #f6f3f8;
    --tone-top: #5a5a5e;
    --tone-charcoal: #2a2a2c;
    --tone-ink: #1c1c1d;
    --tone-graphite: #3c3c3e;
    --tone-stone: #5a5858;
    --tone-ash: #747272;
  }
  html, body {
    margin: 0;
    padding: 0;
    overflow: hidden;
  }
  .vow-poster {
    position: relative;
    width: 1200px;
    height: 2400px;
    overflow: hidden;
    font-family: "Cormorant Garamond", Georgia, serif;
  }
  .backdrop {
    position: absolute;
    inset: 0;
    width: 1200px;
    height: 2400px;
  }
  .section-title {
    position: absolute;
    margin: 0;
    font-weight: 500;
    font-size: 176px;
    line-height: 1;
    color: var(--heading);
    text-shadow: 5px 5px 4px var(--heading-shadow);
    white-space: nowrap;
  }
  .section-title--privileges { left: 149px; top: 120px; }
  .section-title--promises { right: 144px; top: 1116px; }
  .word-list {
    position: absolute;
    margin: 0;
    padding: 0;
    list-style: none;
    font-weight: 300;
    font-size: 100px;
    line-height: 117.6px;
    color: var(--item);
    white-space: nowrap;
  }
  .word-list--privileges { left: 235px; top: 286px; text-align: left; }
  .word-list--promises { right: 137px; top: 1282px; text-align: right; }
</style>
</head>
<body>
  <main class="vow-poster">
    <svg class="backdrop" viewBox="0 0 1200 2400" role="img" aria-label="Faceted backdrop in graphite, charcoal and stone grey tones">
      <defs>
        <linearGradient id="backdrop-tone" x1="0" y1="0" x2="0.35" y2="1">
          <stop offset="0" stop-color="var(--tone-top)"/>
          <stop offset="0.2" stop-color="var(--tone-charcoal)"/>
          <stop offset="0.42" stop-color="var(--tone-ink)"/>
          <stop offset="0.62" stop-color="var(--tone-graphite)"/>
          <stop offset="0.82" stop-color="var(--tone-stone)"/>
          <stop offset="1" stop-color="var(--tone-ash)"/>
        </linearGradient>
      </defs>
      <rect width="1200" height="2400" fill="url(#backdrop-tone)"/>
    </svg>

    <h2 class="section-title section-title--privileges">Privileges</h2>
    <ul class="word-list word-list--privileges">
      <li>Rest of My Life</li>
      <li>Protection</li>
      <li>Provision</li>
      <li>Love – Regardless</li>
      <li>Care</li>
      <li>Purpose</li>
      <li>Patience</li>
    </ul>

    <h2 class="section-title section-title--promises">Promises</h2>
    <ul class="word-list word-list--promises">
      <li>Fight</li>
      <li>Safety</li>
      <li>Cherish</li>
      <li>Unconditional Support</li>
      <li>Listen</li>
      <li>By Your Side</li>
      <li>The Best In You</li>
      <li>The Best In Me</li>
    </ul>
  </main>
</body>
</html>
```